Step and Repeat Backdrop for wedding reception photo booth

Would like to have a Step and Repeat Backdrop (8 foot high by 10 foot wide) that incorporates the wedding logo (attached) and the names Elena and Gavin. Background should be white, and wedding colors are burgundy and gold. Show me creativity :-) I have included some random samples.

```html
<!DOCTYPE html>
<html lang="en">
<head>
<meta charset="utf-8">
<title>Elena &amp; Gavin – Step and Repeat Backdrop</title>
<link rel="stylesheet" href="https://fonts.googleapis.com/css2?family=Pinyon+Script&family=Playfair+Display:wght@400&display=swap">
<style>
  :root {
    --paper: #ffffff;
    --rose: #e0607e;
    --gold: #e6c241;
    --gold-deep: #c99a1c;
    --burgundy: #761a38;
    --repeat-grey: #e9e9ec;
  }
  html, body {
    margin: 0;
    padding: 0;
    width: 1200px;
    height: 959px;
    overflow: hidden;
    background: var(--paper);
  }
  .backdrop {
    position: relative;
    width: 1200px;
    height: 959px;
    background: var(--paper);
    overflow: hidden;
  }
  .backdrop-art {
    position: absolute;
    inset: 0;
  }
  .couple-title {
    position: absolute;
    left: 0;
    top: 150px;
    width: 1200px;
    height: 200px;
    margin: 0;
    font-weight: 400;
  }
  .couple-title .name {
    position: absolute;
    top: 58px;
    font-family: "Pinyon Script", cursive;
    font-size: 84px;
    line-height: 1;
    color: var(--rose);
    z-index: 2;
  }
  .couple-title .name-bride { left: 338px; }
  .couple-title .name-groom { left: 692px; }
  .couple-title .ampersand {
    position: absolute;
    left: 550px;
    top: -36px;
    font-family: "Playfair Display", serif;
    font-size: 240px;
    line-height: 1;
    color: var(--gold);
    opacity: 0.95;
    z-index: 1;
  }
  .heart-name,
  .repeat-name {
    font-family: "Pinyon Script", cursive;
  }
</style>
</head>
<body>
<main class="backdrop">
  <svg class="backdrop-art" width="1200" height="959" viewBox="0 0 1200 959" xmlns="http://www.w3.org/2000/svg">
    <defs>
      <pattern id="name-repeat" width="120" height="56" patternUnits="userSpaceOnUse" patternTransform="rotate(-12)">
        <text class="repeat-name" x="4" y="20" font-size="15" fill="var(--repeat-grey)">Elena &amp; Gavin</text>
        <text class="repeat-name" x="64" y="48" font-size="15" fill="var(--repeat-grey)">Elena &amp; Gavin</text>
      </pattern>
      <radialGradient id="pale-bloom" cx="50%" cy="50%" r="50%">
        <stop offset="0%" stop-color="#f7d3da"/>
        <stop offset="60%" stop-color="#f9dfe4" stop-opacity="0.8"/>
        <stop offset="100%" stop-color="#ffffff" stop-opacity="0"/>
      </radialGradient>
      <radialGradient id="bright-bloom" cx="50%" cy="50%" r="50%">
        <stop offset="0%" stop-color="#f08e9e"/>
        <stop offset="65%" stop-color="#f4b3c2" stop-opacity="0.85"/>
        <stop offset="100%" stop-color="#ffffff" stop-opacity="0"/>
      </radialGradient>
      <radialGradient id="leaf-haze" cx="50%" cy="50%" r="50%">
        <stop offset="0%" stop-color="#c9d9e3" stop-opacity="0.8"/>
        <stop offset="100%" stop-color="#ffffff" stop-opacity="0"/>
      </radialGradient>
      <linearGradient id="sprig-tone" x1="0" y1="0" x2="0" y2="1">
        <stop offset="0%" stop-color="#a57fd0" stop-opacity="0.55"/>
        <stop offset="100%" stop-color="#8a5bb8" stop-opacity="0.35"/>
      </linearGradient>
      <linearGradient id="gold-foil" x1="0" y1="0" x2="1" y2="1">
        <stop offset="0%" stop-color="#f3d35a"/>
        <stop offset="50%" stop-color="#e2b62a"/>
        <stop offset="100%" stop-color="#f0cd4c"/>
      </linearGradient>
      <path id="heart-shape" d="M50 88 C20 66 0 46 0 26 C0 10 12 0 26 0 C38 0 46 8 50 17 C54 8 62 0 74 0 C88 0 100 10 100 26 C100 46 80 66 50 88Z"/>
    </defs>

    <rect class="name-repeat" x="0" y="0" width="1200" height="959" fill="url(#name-repeat)" role="img" aria-label="Faint repeating couple names across the backdrop"/>

    <g role="img" aria-label="Watercolour pale pink peonies and blue leaves, top left corner">
      <ellipse cx="80" cy="120" rx="150" ry="130" fill="url(#pale-bloom)"/>
      <ellipse cx="90" cy="230" rx="120" ry="110" fill="url(#pale-bloom)"/>
      <ellipse cx="190" cy="60" rx="110" ry="70" fill="url(#leaf-haze)"/>
    </g>
    <g role="img" aria-label="Watercolour pale pink peonies and blue leaves, top right corner">
      <ellipse cx="1120" cy="110" rx="150" ry="130" fill="url(#pale-bloom)"/>
      <ellipse cx="1110" cy="230" rx="120" ry="110" fill="url(#pale-bloom)"/>
      <ellipse cx="1010" cy="80" rx="110" ry="70" fill="url(#leaf-haze)"/>
      <ellipse cx="1140" cy="430" rx="80" ry="130" fill="url(#leaf-haze)"/>
    </g>
    <g role="img" aria-label="Watercolour pale pink roses and blue leaves, bottom left corner">
      <ellipse cx="90" cy="880" rx="160" ry="120" fill="url(#pale-bloom)"/>
      <ellipse cx="60" cy="560" rx="70" ry="140" fill="url(#leaf-haze)"/>
    </g>
    <g role="img" aria-label="Watercolour pale pink roses and blue leaves, bottom right corner">
      <ellipse cx="1110" cy="870" rx="170" ry="130" fill="url(#pale-bloom)"/>
      <ellipse cx="1150" cy="680" rx="70" ry="120" fill="url(#leaf-haze)"/>
    </g>

    <g role="img" aria-label="Watercolour coral rose and pink peony, top centre">
      <ellipse cx="560" cy="25" rx="75" ry="55" fill="url(#bright-bloom)"/>
      <ellipse cx="690" cy="40" rx="100" ry="75" fill="url(#bright-bloom)"/>
      <ellipse cx="820" cy="70" rx="70" ry="40" fill="url(#leaf-haze)"/>
    </g>
    <g role="img" aria-label="Watercolour coral rose and pink peony, bottom centre">
      <ellipse cx="530" cy="880" rx="90" ry="90" fill="url(#bright-bloom)"/>
      <ellipse cx="625" cy="910" rx="110" ry="80" fill="url(#bright-bloom)"/>
    </g>

    <g role="img" aria-label="Watercolour purple wildflower sprigs along the left of the ring">
      <ellipse cx="300" cy="220" rx="130" ry="60" fill="url(#sprig-tone)" opacity="0.45"/>
      <ellipse cx="230" cy="420" rx="60" ry="180" fill="url(#sprig-tone)" opacity="0.4"/>
      <ellipse cx="250" cy="720" rx="70" ry="100" fill="url(#sprig-tone)" opacity="0.4"/>
    </g>
    <g role="img" aria-label="Watercolour purple wildflower sprigs along the lower right of the ring">
      <ellipse cx="960" cy="730" rx="80" ry="70" fill="url(#sprig-tone)" opacity="0.4"/>
    </g>

    <g class="gold-rings" fill="none">
      <circle cx="625" cy="495" r="418" stroke="var(--gold-deep)" stroke-width="2.5"/>
      <circle cx="632" cy="490" r="410" stroke="var(--gold)" stroke-width="3"/>
      <circle cx="618" cy="500" r="405" stroke="#f1dc7a" stroke-width="2"/>
    </g>

    <g class="heart heart-gold" transform="translate(222 118) rotate(-8 67 60) scale(1.34)">
      <use href="#heart-shape" fill="url(#gold-foil)"/>
      <text class="heart-name" x="50" y="40" text-anchor="middle" font-size="15" fill="#ffffff">Elena &amp; Gavin</text>
    </g>
    <g class="heart heart-burgundy" transform="translate(488 52) rotate(10 43 39) scale(0.87)">
      <use href="#heart-shape" fill="var(--burgundy)"/>
      <text class="heart-name" x="50" y="40" text-anchor="middle" font-size="15" fill="var(--gold)">Elena &amp; Gavin</text>
    </g>
    <g class="heart heart-gold" transform="translate(665 70) scale(1.12)">
      <use href="#heart-shape" fill="url(#gold-foil)"/>
      <text class="heart-name" x="50" y="40" text-anchor="middle" font-size="15" fill="#ffffff">Elena &amp; Gavin</text>
    </g>
    <g class="heart heart-burgundy" transform="translate(823 125) rotate(12 65 58) scale(1.3)">
      <use href="#heart-shape" fill="var(--burgundy)"/>
      <text class="heart-name" x="50" y="40" text-anchor="middle" font-size="15" fill="var(--gold)">Elena &amp; Gavin</text>
    </g>
    <g class="heart heart-burgundy" transform="translate(154 353) rotate(12 43 39) scale(0.87)">
      <use href="#heart-shape" fill="var(--burgundy)"/>
      <text class="heart-name" x="50" y="40" text-anchor="middle" font-size="15" fill="var(--gold)">Elena &amp; Gavin</text>
    </g>
    <g class="heart heart-gold" transform="translate(985 327) rotate(-8 40 36) scale(0.8)">
      <use href="#heart-shape" fill="url(#gold-foil)"/>
      <text class="heart-name" x="50" y="40" text-anchor="middle" font-size="15" fill="#ffffff">Elena &amp; Gavin</text>
    </g>
    <g class="heart heart-gold" transform="translate(165 545) rotate(10 54 48) scale(1.08)">
      <use href="#heart-shape" fill="url(#gold-foil)"/>
      <text class="heart-name" x="50" y="40" text-anchor="middle" font-size="15" fill="#ffffff">Elena &amp; Gavin</text>
    </g>
    <g class="heart heart-burgundy" transform="translate(973 492) rotate(-10 67 60) scale(1.34)">
      <use href="#heart-shape" fill="var(--burgundy)"/>
      <text class="heart-name" x="50" y="40" text-anchor="middle" font-size="15" fill="var(--gold)">Elena &amp; Gavin</text>
    </g>
    <g class="heart heart-gold" transform="translate(202 716) rotate(8 38 34) scale(0.76)">
      <use href="#heart-shape" fill="url(#gold-foil)"/>
      <text class="heart-name" x="50" y="40" text-anchor="middle" font-size="15" fill="#ffffff">Elena &amp; Gavin</text>
    </g>
    <g class="heart heart-gold" transform="translate(926 740) rotate(-6 56 50) scale(1.12)">
      <use href="#heart-shape" fill="url(#gold-foil)"/>
      <text class="heart-name" x="50" y="40" text-anchor="middle" font-size="15" fill="#ffffff">Elena &amp; Gavin</text>
    </g>
    <g class="heart heart-burgundy" transform="translate(336 834) rotate(-6 54 48) scale(1.08)">
      <use href="#heart-shape" fill="var(--burgundy)"/>
      <text class="heart-name" x="50" y="40" text-anchor="middle" font-size="15" fill="var(--gold)">Elena &amp; Gavin</text>
    </g>
    <g class="heart heart-burgundy" transform="translate(688 835) rotate(14 63 56) scale(1.26)">
      <use href="#heart-shape" fill="var(--burgundy)"/>
      <text class="heart-name" x="50" y="40" text-anchor="middle" font-size="15" fill="var(--gold)">Elena &amp; Gavin</text>
    </g>
  </svg>

  <h1 class="couple-title">
    <span class="name name-bride">Elena</span>
    <span class="ampersand">&amp;</span>
    <span class="name name-groom">Gavin</span>
  </h1>
</main>
</body>
</html>
```